Norvale LLC
256-318-4702
463 Parry K. Holden Blvd.
Sylacauga, AL 35162
norvalellc97@quillmail.example

Heavy& Light Duty Diesel Truck, Trailer, and Equipment Repair
Certified QTB Master Tech & trained techs

Services:
alignments, brakes, suspension, A/C, engine overhauls, RVM inspections, fleet maintenance, computer diagnosis for gas & diesel, warranty work, performance parts for all diesel pickups, Welding & fabrication

Colors, text for Company, phone number, email address in bright red, all other text black.
background color of postcard light grey, black border around pictures.

Colors
ec2027

```html
<!DOCTYPE html>
<html lang="en">
<head>
<meta charset="utf-8">
<title>Norvale LLC Truck Repair Shop Postcard</title>
<link rel="stylesheet" href="https://fonts.googleapis.com/css2?family=Roboto:wght@700;900&family=Roboto+Condensed:wght@700&display=swap">
<style>
  :root {
    --brand-red: #ec2027;
    --ink: #111111;
    --frame: #000000;
    --silver-light: #f4f4f4;
    --silver-mid: #d6d6d6;
    --silver-dark: #b9b9b9;
    --band-dark: #4a4a4a;
    --band-light: #9a9a9a;
    --white: #ffffff;
  }
  * { margin: 0; padding: 0; box-sizing: border-box; }
  html, body {
    width: 1200px;
    height: 922px;
    overflow: hidden;
    background: var(--silver-mid);
  }
  .postcard {
    position: relative;
    width: 1200px;
    height: 922px;
    background: linear-gradient(100deg, var(--silver-dark) 0%, var(--silver-light) 22%, var(--silver-mid) 45%, var(--silver-light) 70%, var(--silver-dark) 100%);
    font-family: "Roboto Condensed", "Arial Narrow", sans-serif;
    color: var(--ink);
  }
  .masthead {
    position: absolute;
    left: 47px;
    top: 38px;
    width: 1122px;
    height: 110px;
    border-bottom: 2px solid var(--ink);
  }
  .company-name {
    position: absolute;
    left: 0;
    top: 0;
    font-family: "Roboto Condensed", "Arial Narrow", sans-serif;
    font-weight: 700;
    font-size: 96px;
    line-height: 96px;
    color: var(--brand-red);
    text-transform: uppercase;
    letter-spacing: 2px;
  }
  .shop-type {
    position: absolute;
    right: 0;
    top: 30px;
    font-weight: 700;
    font-size: 64px;
    line-height: 64px;
    color: var(--ink);
  }
  .tagline {
    position: absolute;
    left: 0;
    width: 100%;
    text-align: center;
    font-family: "Roboto", Arial, sans-serif;
    font-weight: 700;
    font-size: 29px;
    letter-spacing: 1.6px;
    color: var(--ink);
  }
  .tagline--scope { top: 165px; }
  .tagline--certified { top: 215px; }
  .photo-strip {
    position: absolute;
    left: 0;
    top: 273px;
    width: 1200px;
    height: 287px;
    background: var(--frame);
    display: flex;
    gap: 7px;
    padding: 5px;
  }
  .photo {
    flex: 1;
    height: 100%;
  }
  .photo--truck-bay {
    background: linear-gradient(90deg, #1c1f55 0%, #3a3c6c 30%, #b8b8b4 55%, #d9d6cc 80%, #9a938a 100%);
  }
  .photo--diagnostics {
    background: radial-gradient(ellipse at 45% 45%, #5a5a60 0%, #2a2a2e 45%, #4b4a55 100%);
  }
  .photo--shop-front {
    background: linear-gradient(180deg, #6f8fb8 0%, #5d6b48 30%, #d8d6cc 45%, #c9c5b8 70%, #a59e90 100%);
  }
  .services-band {
    position: absolute;
    left: 0;
    top: 564px;
    width: 1196px;
    height: 44px;
    background: linear-gradient(90deg, var(--band-dark) 0%, var(--band-dark) 70%, var(--band-light) 100%);
    text-align: center;
    font-family: "Roboto", Arial, sans-serif;
    font-weight: 700;
    font-size: 27px;
    line-height: 44px;
    letter-spacing: 14px;
    color: var(--white);
    padding-left: 8px;
  }
  .services-list {
    position: absolute;
    left: 0;
    top: 614px;
    width: 100%;
    text-align: center;
    list-style: none;
    font-weight: 700;
    font-size: 30px;
    line-height: 36px;
    color: var(--ink);
  }
  .contact {
    position: absolute;
    left: 0;
    width: 100%;
    text-align: center;
    font-family: "Roboto", Arial, sans-serif;
    font-weight: 700;
    color: var(--brand-red);
  }
  .contact--phone { top: 745px; font-size: 62px; letter-spacing: 3px; }
  .contact--address { top: 814px; font-size: 37px; letter-spacing: 2px; }
  .contact--email { top: 862px; font-size: 29px; letter-spacing: 1px; }
</style>
</head>
<body>
  <main class="postcard">
    <header class="masthead">
      <h1 class="company-name">Norvale LLC</h1>
      <p class="shop-type">Truck Repair Shop</p>
    </header>

    <p class="tagline tagline--scope">Heavy&amp; Light Duty Diesel Truck, Trailer, and Equipment Repair</p>
    <p class="tagline tagline--certified">Certified QTB Master Tech &amp; trained techs</p>

    <section class="photo-strip">
      <div class="photo photo--truck-bay" role="img" aria-label="Photo of a semi truck parked in the alignment bay beside a wheel alignment machine"></div>
      <div class="photo photo--diagnostics" role="img" aria-label="Photo of a technician's hands holding a diagnostic scan tablet"></div>
      <div class="photo photo--shop-front" role="img" aria-label="Photo of the shop building with pickup trucks and a service truck out front"></div>
    </section>

    <div class="services-band">SERVICES:</div>
    <ul class="services-list">
      <li>Alignments • Brakes • Suspension • A/C • Engine Overhauls • RVM Inspections</li>
      <li>Fleet Maintenance • Computer Diagnosis For Gas &amp; Diesel • Warranty Work</li>
      <li>Performance Parts For All Diesel Pickups • Welding &amp; Fabrication</li>
    </ul>

    <p class="contact contact--phone">256.318.4702</p>
    <p class="contact contact--address">463 Parry K. Holden Blvd. Sylacauga, AL 35162</p>
    <p class="contact contact--email">norvalellc97@quillmail.example</p>
  </main>
</body>
</html>
```